Silverleaf Rise Accounting Program

size of ad Full: 7” x 9.6”
1- this is for a ladies program so it should appeal to women.
2-however, I do not want any pictures of people in this ad.
3-all the text should be seen and not covered over by graphics.
4-It should be an ad that will draw people's attention and people should look at it and say it looks nice I want to see that ad.
5-I have put all the instructions in yellow in the file below.
6-please leave 1 inch for the footer .
good luck with this project

• no picture or vector of people.

```html
<!DOCTYPE html>
<html lang="en">
<head>
<meta charset="utf-8">
<title>Silverleaf Rise Accounting Program — Attention Women</title>
<link rel="stylesheet" href="https://fonts.googleapis.com/css2?family=Cinzel:wght@700;900&family=Great+Vibes&family=Montserrat:wght@300;400;500;600;700&display=swap">
<style>
  :root {
    --magenta: #ec008c;
    --white: #ffffff;
    --ink: #1a1a1a;
    --footer-grey: #e9e9e9;
    --backdrop: #d6d6d6;
    --serif: "Cinzel", "Times New Roman", serif;
    --script: "Great Vibes", cursive;
    --sans: "Montserrat", Arial, sans-serif;
  }
  * { margin: 0; padding: 0; box-sizing: border-box; }
  html, body { width: 1200px; height: 2285px; overflow: hidden; background: var(--backdrop); }
  .ad {
    position: absolute; left: 66px; top: 411px;
    width: 1067px; height: 1463px;
    background: var(--white); overflow: hidden;
    box-shadow: 0 2px 8px rgba(0,0,0,.25);
    font-family: var(--sans); color: var(--ink);
  }
  .ad-shapes { position: absolute; inset: 0; }
  .abs { position: absolute; }

  .headline-attention { left: 45px; top: 96px; font-family: var(--serif); font-weight: 700; font-size: 78px; color: var(--white); letter-spacing: 1px; line-height: 1; }
  .headline-women { left: 52px; top: 150px; font-family: var(--script); font-size: 150px; color: var(--white); line-height: 1; }
  .headline-rule { left: 147px; top: 305px; width: 233px; height: 5px; background: var(--white); }

  .degree-title { left: 665px; top: 100px; font-family: var(--serif); font-weight: 700; font-size: 50px; line-height: 56px; color: var(--magenta); }
  .degree-rule { left: 665px; top: 275px; width: 232px; height: 5px; background: var(--magenta); }
  .degree-copy { left: 665px; top: 300px; font-size: 23.5px; line-height: 28px; color: var(--ink); }

  .banner { left: 94px; top: 528px; width: 874px; height: 89px; display: flex; border: 2px solid var(--magenta); }
  .banner-name { width: 450px; display: flex; align-items: center; justify-content: center; font-family: var(--serif); font-weight: 700; font-size: 64px; color: var(--magenta); }
  .banner-tag { flex: 1; background: var(--magenta); color: var(--white); display: flex; align-items: center; justify-content: center; font-weight: 700; font-size: 27px; letter-spacing: .5px; }

  .stat { top: 640px; width: 272px; height: 225px; border: 2px dashed var(--magenta); border-radius: 30px; text-align: center; color: var(--ink); }
  .stat-number { font-size: 66px; font-weight: 400; color: var(--magenta); line-height: 1; margin-top: 42px; }
  .stat-number.tight { margin-top: 28px; }
  .stat-label { font-size: 26px; line-height: 29px; margin-top: 12px; text-transform: uppercase; }

  .burst-text { left: 48px; top: 1000px; width: 330px; text-align: center; color: var(--white); font-weight: 700; }
  .burst-small { font-size: 27px; line-height: 30px; }
  .burst-big { font-size: 104px; line-height: 92px; font-weight: 700; letter-spacing: -3px; }

  .ranking-caption { left: 345px; top: 1190px; width: 290px; text-align: center; font-size: 16.5px; line-height: 19px; }
  .ranking-caption strong { font-weight: 700; }

  .divider { left: 647px; top: 1020px; width: 2px; height: 265px; background: var(--ink); }

  .event { left: 665px; top: 1038px; }
  .event-kicker { font-size: 21px; }
  .event-date { font-size: 46px; font-weight: 700; color: var(--magenta); line-height: 52px; }
  .event-time { font-size: 23px; font-weight: 700; margin-bottom: 14px; }
  .event-note { font-size: 21px; line-height: 25px; }
  .contact-line { display: flex; align-items: center; gap: 14px; font-size: 21px; line-height: 30px; font-weight: 500; }
  .contact-line svg { width: 18px; height: 18px; }
</style>
</head>
<body>
<main class="ad" aria-label="Silverleaf Rise Accounting Program advertisement">
  <svg class="ad-shapes" width="1067" height="1463" viewBox="0 0 1067 1463" aria-hidden="true">
    <rect class="footer-band" x="0" y="1310" width="1067" height="153" fill="var(--footer-grey)"/>
    <circle class="hero-disc" cx="160" cy="45" r="435" fill="var(--magenta)"/>
    <path class="hero-arc" d="M595 0 C640 200 520 420 292 488 C560 430 690 230 647 0 Z" fill="var(--magenta)"/>
    <path class="lower-sweep" d="M330 990 C560 880 850 870 1067 1073 L1067 1123 C900 950 600 920 330 990 Z" fill="var(--magenta)"/>
    <path class="lower-sweep-line" d="M480 982 C680 915 820 920 930 975" fill="none" stroke="var(--white)" stroke-width="3"/>
    <path class="corner-sweep" d="M0 1325 C30 1270 70 1222 110 1192 L104 1210 C60 1255 25 1315 0 1375 Z" fill="var(--magenta)"/>
    <path class="corner-sweep-line" d="M0 1390 C35 1320 70 1275 110 1235" fill="none" stroke="var(--magenta)" stroke-width="8"/>
    <polygon class="starburst" transform="translate(213 1120)" fill="var(--magenta)"
      points="165,0 126,22 155,56 111,64 126,106 82,98 83,143 44,120 29,162 0,128 -29,162 -44,120 -83,143 -82,98 -126,106 -111,64 -155,56 -126,22 -165,0 -126,-22 -155,-56 -111,-64 -126,-106 -82,-98 -83,-143 -44,-120 -29,-162 0,-128 29,-162 44,-120 83,-143 82,-98 126,-106 111,-64 155,-56 126,-22"/>
    <circle class="ranking-badge" cx="490" cy="1120" r="44" fill="#f39a2b" role="img" aria-label="Program ranking badge"/>
  </svg>

  <h1>
    <span class="abs headline-attention">ATTENTION</span>
    <span class="abs headline-women">Women</span>
  </h1>
  <div class="abs headline-rule"></div>

  <h2 class="abs degree-title">A MASTER’S<br>DEGREE IN<br>ACCOUNTING</h2>
  <div class="abs degree-rule"></div>
  <p class="abs degree-copy">A stable, lucrative<br>career, with high-paying,<br>full /part time opportunities<br>in Private/Public companies</p>

  <div class="abs banner">
    <div class="banner-name">THE BPS JOB</div>
    <div class="banner-tag">PLACEMENT ADVANTAGE</div>
  </div>

  <div class="abs stat" style="left:104px"><div class="stat-number">96%</div><div class="stat-label">Placement<br>Rate</div></div>
  <div class="abs stat" style="left:395px"><div class="stat-number">06</div><div class="stat-label">Placement<br>Directors</div></div>
  <div class="abs stat" style="left:686px"><div class="stat-number tight">100’S</div><div class="stat-label">Relationships<br>with decades<br>firms</div></div>

  <div class="abs burst-text">
    <div class="burst-small">MASTERS IN</div>
    <div class="burst-big">12</div>
    <div class="burst-small">MONTHS</div>
  </div>

  <p class="abs ranking-caption"><strong>Hollowbrook University</strong>,<br>Masters in Accounting program,<br>received the highest possible<br>rating in USA</p>

  <div class="abs divider"></div>

  <div class="abs event">
    <div class="event-kicker">Zoom open house</div>
    <div class="event-date">June 14</div>
    <div class="event-time">SUNDAY, 2 p.m.</div>
    <div class="event-note">for a zoom&nbsp; link /<br>conference number /information</div>
    <div class="contact-line">
      <svg viewBox="0 0 18 18"><rect x="1" y="4" width="16" height="11" fill="var(--magenta)"/><path d="M1 4 L9 10 L17 4" fill="none" stroke="var(--white)" stroke-width="1.5"/></svg>
      nj@nj.brightpathjobs.org
    </div>
    <div class="contact-line">
      <svg viewBox="0 0 18 18"><path d="M4 2 L7 2 L8 6 L6 7.5 C7 10 8.5 11.5 11 12.5 L12.5 10.5 L16 11.5 L16 15 C9 15.5 2.5 9 3 2 Z" fill="var(--magenta)"/></svg>
      555 014 2200x 111
    </div>
  </div>
</main>
</body>
</html>
```